Simple HTML Design Needed

We're looking for a simple yet elegant HTML design that will be used for a custom wordpress theme.

We're fairly open to design ideas, but the final product will incorporate elements from the following examples:

http://www.pixomarl.com/widecanvas/
http://layoutbrook.com/demo/tidewell/
http://www.gluvena.at/themedemo/?theme=orbane

We just need the homepage HTML and CSS; we'll create the rest of the pages, unless you want to go above an beyond.

The most creative design will win!

```html
<!DOCTYPE html>
<html lang="en">
<head>
<meta charset="utf-8">
<title>Crest business company</title>
<link href="https://fonts.googleapis.com/css2?family=Open+Sans:wght@300;400;600;700&family=Arimo:ital,wght@0,400;0,700;1,700&display=swap" rel="stylesheet">
<style>
:root{
  --orange:#e8772e;
  --plum:#6a1d40;
  --olive:#c3b14c;
  --ink:#2b2b2b;
  --grey:#c9c9c9;
  --mid:#8c8c8c;
  --line:#dedede;
  --panel:#ffffff;
  --page:#f3f3f3;
  --band:#e9e9e9;
  --link:#4a6d8c;
}
*{box-sizing:border-box;margin:0;padding:0}
html,body{width:957px;height:1200px;overflow:hidden}
body{background:var(--page);font-family:"Arimo",Arial,sans-serif;color:var(--ink);position:relative}
.page{position:relative;width:957px;height:1200px;background:linear-gradient(#fff 0,#fff 500px,var(--page) 500px)}
.brand{position:absolute;left:72px;top:30px;display:flex;align-items:flex-end;gap:8px}
.brand-name{font-family:"Open Sans",sans-serif;font-weight:600;font-size:58px;line-height:1;color:#333;letter-spacing:-2px}
.brand-tag{font-family:"Open Sans",sans-serif;font-size:13px;line-height:14px;color:var(--mid);padding-bottom:8px}
.nav{position:absolute;left:38px;top:113px;width:889px;height:47px;border:1px solid var(--line);background:#fff;display:flex;align-items:center;padding-left:40px}
.nav a{font-family:"Open Sans",sans-serif;font-size:14px;color:var(--ink);text-decoration:none;padding:0 48px;border-left:1px solid var(--line);line-height:22px}
.nav a:first-child{border-left:none;padding-left:0;color:var(--orange);opacity:.75}
.hero-photo{position:absolute;left:610px;top:0;width:330px;height:500px;background:radial-gradient(ellipse at 55% 35%,#d8d8d8,#efefef 60%,rgba(255,255,255,0) 80%)}
.hero-title{position:absolute;left:70px;top:208px;font-family:"Open Sans",sans-serif;font-weight:300;line-height:1.05}
.hero-title .l1{font-size:66px;color:var(--orange);letter-spacing:-1px}
.hero-title .l2{font-size:50px;color:var(--orange)}
.hero-title .l2 .soft{color:var(--grey)}
.hero-title .l3{font-size:50px;color:var(--grey)}
.more{font-family:"Arimo",sans-serif;font-size:11px;font-weight:700;color:var(--link);text-decoration:underline;text-transform:uppercase}
.hero-more{position:absolute;left:72px;top:418px;color:var(--orange)}
.content{position:absolute;left:38px;top:508px;width:889px;height:648px;background:var(--panel);border:1px solid var(--line)}
.circles{position:absolute;left:277px;top:435px;display:flex;gap:0}
.circle{width:141px;height:141px;border-radius:50%;display:flex;align-items:center;justify-content:center;text-align:center;color:#fff;font-family:"Open Sans",sans-serif;font-size:16px;line-height:19px;border:4px solid #fff}
.circle.plum{background:var(--plum)}
.circle.orange{background:var(--orange);flex-direction:column}
.circle.olive{background:var(--olive)}
.intro{position:absolute;top:93px;left:0;width:100%;text-align:center;font-family:"Open Sans",sans-serif;font-weight:700;font-size:28px;line-height:34px;color:var(--grey)}
.steps{position:absolute;top:190px;left:38px;display:flex;gap:22px}
.step{width:190px;display:flex;gap:8px}
.step-letter{font-family:"Open Sans",sans-serif;font-weight:700;font-size:32px;line-height:32px}
.step p{font-size:9.5px;line-height:13px}
.step .more{display:block;margin-top:12px;margin-left:-38px}
.s-a .step-letter,.s-a p{color:var(--plum)}
.s-b .step-letter,.s-b p{color:var(--orange)}
.s-c .step-letter,.s-c p{color:var(--olive)}
.s-d .step-letter,.s-d p{color:var(--grey)}
.divider{position:absolute;top:305px;left:0;width:100%;border-top:1px solid var(--line)}
.welcome{position:absolute;left:36px;top:335px;width:560px}
h2{font-family:"Open Sans",sans-serif;font-weight:700;font-size:29px;color:var(--ink)}
.welcome p{font-size:10px;line-height:15px;color:#666;margin-top:14px}
.welcome p a{color:var(--link)}
.team{display:flex;gap:10px;margin-top:22px}
.member{width:178px}
.member-photo{height:123px;border:1px solid var(--line);background:linear-gradient(#e4e4e4,#bdbdbd)}
.member-name{text-align:right;font-weight:700;font-style:italic;font-size:12px;margin-top:14px}
.member-role{text-align:right;font-size:9px;color:var(--mid);text-transform:uppercase}
.news{position:absolute;left:638px;top:335px;width:213px}
.news-item{border-bottom:1px solid var(--line);padding:14px 0 18px}
.news-date{font-size:11px;color:var(--ink)}
.news-item p{font-size:9.5px;line-height:14px;color:var(--mid);margin-top:6px}
.news .more{display:block;text-align:right;margin-top:18px;color:var(--mid)}
.band{position:absolute;left:0;top:1156px;width:957px;height:44px;background:var(--band)}
.band-cols{position:absolute;left:75px;top:18px;display:flex;gap:0}
.band-cols h3{width:188px;font-family:"Open Sans",sans-serif;font-weight:700;font-size:22px;color:var(--ink)}
</style>
</head>
<body>
<div class="page">
  <div class="hero-photo" role="img" aria-label="Photo of a smiling businesswoman making a victory sign"></div>

  <div class="brand">
    <span class="brand-name">Crest</span>
    <span class="brand-tag">business<br>company</span>
  </div>

  <nav class="nav">
    <a href="#">home</a><a href="#">about</a><a href="#">services</a><a href="#">products</a><a href="#">contacts</a>
  </nav>

  <div class="hero-title">
    <div class="l1">WeREPRESENT</div>
    <div class="l2"><span class="soft">a</span> HUGE EXPERIENCE</div>
    <div class="l3">intellectual potential</div>
  </div>
  <a class="more hero-more" href="#">Read more</a>

  <section class="content">
    <p class="intro">Our experience is the base for<br>your innovations.</p>

    <div class="steps">
      <div class="step s-a"><span class="step-letter">A.</span><div><p>Vivamus hendrerit mauris ut dui gravida ut viverra lectus tincidunt cras mattis.</p><a class="more" href="#">Read more</a></div></div>
      <div class="step s-b"><span class="step-letter">B.</span><div><p>Cras mattis tempor eros nec tristique sed sed felis arcu vel vehicula augue.</p><a class="more" href="#">Read more</a></div></div>
      <div class="step s-c"><span class="step-letter">C.</span><div><p>Sed sed felis arcu vel vehicula maecenas faucibus sagittis cursus fusce tincidunt.</p><a class="more" href="#">Read more</a></div></div>
      <div class="step s-d"><span class="step-letter">D.</span><div><p>Cras mattis tempor eros nec tristique. Sed sed felis arcu, vel vehicula augue. Maecenas faucibus cursus fusce tincidunt tellus eget tristique cursus.</p><a class="more" href="#">Read more</a></div></div>
    </div>

    <div class="divider"></div>

    <div class="welcome">
      <h2>Welcome to our company!</h2>
      <p><a href="#">Click here</a> for more info about this free website template created by LayoutForge.com. This website template is optimized for 1280X1024 screen resolution. It is also XHTML &amp; CSS valid. Vivamus hendrerit mauris ut dui gravida ut viverra lectus tincidunt. Cras mattis tempor eros nec tristique.</p>
      <div class="team">
        <div class="member"><div class="member-photo" role="img" aria-label="Portrait of a smiling female manager"></div><div class="member-name">Nora Vale</div><div class="member-role">Manager</div></div>
        <div class="member"><div class="member-photo" role="img" aria-label="Portrait of a male marketologist"></div><div class="member-name">Leo Marsh</div><div class="member-role">Marketologist</div></div>
        <div class="member"><div class="member-photo" role="img" aria-label="Portrait of a smiling female manager"></div><div class="member-name">Dana Reyes</div><div class="member-role">Manager</div></div>
      </div>
    </div>

    <aside class="news">
      <h2>Latest news:</h2>
      <div class="news-item"><div class="news-date">NOV. 26, 2012</div><p>The PSD source files of this Crest template are available for free for the registered members of LayoutForge.com. Feel free to get them!</p></div>
      <div class="news-item"><div class="news-date">NOV. 20, 2012</div><p>This website template has several pages: Home, About, Services, Products, Contacts (note that contact us form - doesn't work)</p></div>
      <a class="more" href="#">Read more</a>
    </aside>
  </section>

  <div class="circles">
    <div class="circle plum">BUSINESS<br>STRATEGY</div>
    <div class="circle orange"><svg width="22" height="12" viewBox="0 0 22 12" aria-hidden="true"><polyline points="2,10 11,2 20,10" fill="none" stroke="#fff" stroke-width="3"/></svg>MARKETING<br>RESEARCH</div>
    <div class="circle olive">FINANCIAL &amp;<br>BANKING</div>
  </div>

  <div class="band">
    <div class="band-cols"><h3>Services:</h3><h3>Solutions:</h3><h3>Programs:</h3><h3>Testimonials:</h3></div>
  </div>
</div>
</body>
</html>
```